Business Card Design Project

I need a business card for a Management Consultancy. We work with organisational design and development and strategic change using facilitation, consulting and coaching.

Size of card is 90 x 55mm.

Logo is attached.

Wording is:

Maria Kestle
Director

tel 0491627358
email is: info@tallowpoint.com.au

Target Market(s)

Government departments and not for profit organisations mainly.

Industry/Entity Type

Business

Requirements
Must have
• White or colour background not black.

On one side of the card, either back or front please include the words:

Leading Strategic Change

Two sided business card

```html
<!DOCTYPE html>
<html lang="en">
<head>
<meta charset="utf-8">
<title>TallowPoint Consulting – Business Card</title>
<link rel="stylesheet" href="https://fonts.googleapis.com/css2?family=Arimo:wght@400;700&display=swap">
<style>
  :root {
    --stage: #343437;
    --card: #f3f3f3;
    --ink: #3b3e44;
    --ink-soft: #5b5f66;
    --blue: #4a9fd0;
    --green: #7bbf3a;
    --rule: #c9cbce;
    --white: #ffffff;
  }
  * { box-sizing: border-box; margin: 0; padding: 0; }
  html, body {
    width: 1200px;
    height: 840px;
    overflow: hidden;
    background: var(--stage);
    font-family: "Arimo", Arial, sans-serif;
  }
  .canvas {
    position: relative;
    width: 1200px;
    height: 840px;
  }
  .card {
    position: absolute;
    top: 255px;
    width: 540px;
    height: 330px;
    background: var(--card);
    border-radius: 24px;
    overflow: hidden;
  }
  .card--info { left: 40px; }
  .card--brand { left: 620px; }

  /* Info side */
  .tagline-band {
    position: absolute;
    left: 0;
    top: 70px;
    width: 252px;
    height: 34px;
    background: var(--ink);
    clip-path: polygon(0 0, 100% 0, calc(100% - 12px) 100%, 0 100%);
    color: var(--white);
    font-size: 15px;
    line-height: 34px;
    padding-left: 22px;
    letter-spacing: 0.2px;
  }
  .accent {
    position: absolute;
    top: 70px;
    width: 12px;
    height: 34px;
    clip-path: polygon(12px 0, 100% 0, 0 100%, 0 100%);
  }
  .accent--blue { left: 254px; background: var(--blue); clip-path: polygon(60% 0, 100% 0, 40% 100%, 0 100%); }
  .accent--green { left: 268px; background: var(--green); clip-path: polygon(60% 0, 100% 0, 40% 100%, 0 100%); }

  .brand-mark {
    display: flex;
    align-items: center;
    gap: 10px;
    color: var(--ink-soft);
    font-weight: 700;
  }
  .brand-mark__dot {
    border-radius: 50%;
    background: var(--blue);
    flex: none;
  }
  .card--info .brand-mark {
    position: absolute;
    left: 296px;
    top: 72px;
    font-size: 15px;
  }
  .card--info .brand-mark__dot { width: 30px; height: 30px; }

  .person {
    position: absolute;
    left: 40px;
    top: 196px;
    color: var(--ink);
  }
  .person__name { font-size: 22px; font-weight: 700; }
  .person__role { font-size: 15px; color: var(--ink-soft); margin-top: 4px; }

  .divider {
    position: absolute;
    left: 290px;
    top: 146px;
    width: 1px;
    height: 112px;
    background: var(--rule);
  }
  .contact {
    position: absolute;
    left: 310px;
    top: 158px;
    list-style: none;
    color: var(--ink);
    font-size: 15px;
  }
  .contact__item {
    display: flex;
    align-items: center;
    gap: 9px;
    height: 24px;
  }
  .contact__icon { width: 16px; height: 16px; flex: none; }

  /* Brand side */
  .card--brand .brand-mark {
    position: absolute;
    inset: 0;
    justify-content: center;
    gap: 18px;
    font-size: 38px;
    line-height: 1.08;
  }
  .card--brand .brand-mark__dot { width: 70px; height: 70px; }
</style>
</head>
<body>
<main class="canvas">

  <section class="card card--info" aria-label="Business card, contact side">
    <div class="tagline-band">Leading Strategic Change</div>
    <span class="accent accent--blue"></span>
    <span class="accent accent--green"></span>

    <div class="brand-mark">
      <span class="brand-mark__dot"></span>
      <span class="brand-mark__name">TallowPoint Consulting</span>
    </div>

    <div class="person">
      <p class="person__name">Maria Kestle</p>
      <p class="person__role">Director</p>
    </div>

    <span class="divider"></span>

    <ul class="contact">
      <li class="contact__item">
        <svg class="contact__icon" viewBox="0 0 16 16" aria-hidden="true">
          <rect width="16" height="16" rx="3" fill="#3b3e44"/>
          <path d="M5 3.5h2l1 2.5-1.3 1a6 6 0 0 0 2.3 2.3l1-1.3 2.5 1v2c0 .6-.4 1-1 1A8 8 0 0 1 4 4.5c0-.6.4-1 1-1z" fill="#ffffff"/>
        </svg>
        <span>0491627358</span>
      </li>
      <li class="contact__item">
        <svg class="contact__icon" viewBox="0 0 16 16" aria-hidden="true">
          <rect width="16" height="16" rx="3" fill="#3b3e44"/>
          <rect x="3" y="4.5" width="10" height="7" rx="1" fill="#ffffff"/>
          <path d="M3.5 5l4.5 3.5L12.5 5" fill="none" stroke="#3b3e44" stroke-width="1"/>
        </svg>
        <span>info@tallowpoint.com.au</span>
      </li>
    </ul>
  </section>

  <section class="card card--brand" aria-label="Business card, brand side">
    <div class="brand-mark">
      <span class="brand-mark__dot"></span>
      <span class="brand-mark__name">TallowPoint<br>Consulting</span>
    </div>
  </section>

</main>
</body>
</html>
```